Financial advisory firm needs new business card design

Business card design , simple , elegant, professional. Will use existing logo. One side should be a solid blue background (matching blue in Logo) . info side should have basic info, maybe two color panes. one white, one a different color..maybe light grey. Please visit our website to get feel for colors and business. www.tallowmeadwealth.com

Industry/Entity Type

Financial Service

Contact Information for Business Card

Basic info..minimalist, modern, approach

Colors

Designer to choose colors to be used in the design.

Requirements
Must have
• Important regulatory requirement. The following disclosure MUST be included somewhere on the business card. It can be either front, or back, and it may be in a smaller font (but has to be legible). My interest is to satisfy the requirement with the least possible disruption to the beauty of the card design.
• All securities offered through the Harrowgate Capital, Inc. Oakhurst Lane, NJ. Member QOLTA/DWEM. Advisory services provided through HC Advisory Services, Inc. an PBR Registered Investment Advisor.

```html
<!DOCTYPE html>
<html lang="en">
<head>
<meta charset="utf-8">
<title>Tallowmead Wealth – Business Card</title>
<link rel="stylesheet" href="https://fonts.googleapis.com/css2?family=Arimo:wght@400;700&display=swap">
<style>
  :root {
    --stage: #e4e6e9;
    --brand-blue: #0d4fa8;
    --deep-blue: #062a78;
    --bright-blue: #1a8fe8;
    --ink: #1b1b1b;
    --muted-ink: #555a60;
    --name-blue: #1f4f8f;
    --paper: #ffffff;
    --rule: #2f62a0;
  }
  * { box-sizing: border-box; margin: 0; padding: 0; }
  html, body { width: 1200px; height: 901px; overflow: hidden; }
  body {
    background: var(--stage);
    font-family: "Arimo", Arial, sans-serif;
    position: relative;
  }
  .card {
    position: absolute;
    left: 320px;
    width: 560px;
    height: 320px;
    border-radius: 4px;
    overflow: hidden;
    box-shadow: 0 6px 18px rgba(0,0,0,0.18);
  }
  .card--front { top: 110px; }
  .card--back { top: 470px; background: var(--paper); }

  .front-art {
    position: absolute; inset: 0;
    background: radial-gradient(ellipse at 60% 55%, var(--bright-blue) 0%, var(--brand-blue) 45%, var(--deep-blue) 100%);
  }
  .wordmark {
    position: absolute;
    font-weight: 700;
    letter-spacing: 1px;
    white-space: nowrap;
  }
  .card--front .wordmark {
    left: 0; right: 0; top: 138px;
    text-align: center;
    font-size: 40px;
    color: var(--paper);
  }
  .card--back .wordmark {
    left: 40px; top: 162px;
    font-size: 25px;
    color: var(--ink);
  }
  .divider {
    position: absolute;
    left: 322px; top: 44px;
    width: 1px; height: 196px;
    background: var(--rule);
  }
  .contact {
    position: absolute;
    left: 342px; top: 52px;
    color: var(--ink);
    font-size: 11px;
    line-height: 1.4;
  }
  .contact__name {
    font-size: 20px; font-weight: 700;
    color: var(--name-blue);
    line-height: 1.1;
  }
  .contact__title { font-size: 12px; margin-bottom: 16px; }
  .contact__address { margin-bottom: 18px; }
  .contact__row {
    display: flex; align-items: center; gap: 9px;
    margin-bottom: 3px;
  }
  .contact__row svg { width: 12px; height: 12px; flex: none; }
  .web-domain { color: var(--name-blue); }
  .disclosure {
    position: absolute;
    left: 40px; right: 40px; bottom: 16px;
    font-size: 8px;
    line-height: 1.4;
    color: var(--muted-ink);
    text-align: center;
  }
</style>
</head>
<body>

<section class="card card--front" aria-label="Card front">
  <div class="front-art" role="img" aria-label="Abstract flowing blue light waves background"></div>
  <div class="wordmark">Tallowmead Wealth</div>
</section>

<section class="card card--back" aria-label="Card back">
  <div class="wordmark">Tallowmead Wealth</div>
  <div class="divider"></div>
  <div class="contact">
    <div class="contact__name">Martin Hale</div>
    <div class="contact__title">President</div>
    <div class="contact__address">48 Fenwick Road, Suite 110<br>Brookvale, NJ 07000</div>
    <div class="contact__row">
      <svg viewBox="0 0 12 12" aria-hidden="true"><path d="M2.5 1h2l1 2.5-1.3 1a6 6 0 0 0 3.3 3.3l1-1.3 2.5 1v2a1 1 0 0 1-1 1A9 9 0 0 1 1.5 2a1 1 0 0 1 1-1z" fill="#1f4f8f"/></svg>
      <span>(555) 240-6183</span>
    </div>
    <div class="contact__row">
      <svg viewBox="0 0 12 12" aria-hidden="true"><rect x="1" y="2.5" width="10" height="7" fill="none" stroke="#1f4f8f"/><path d="M1 2.5l5 4 5-4" fill="none" stroke="#1f4f8f"/></svg>
      <span>info@tallowmeadwealth.com</span>
    </div>
    <div class="contact__row">
      <svg viewBox="0 0 12 12" aria-hidden="true"><circle cx="6" cy="6" r="5" fill="none" stroke="#1f4f8f"/><ellipse cx="6" cy="6" rx="2.2" ry="5" fill="none" stroke="#1f4f8f"/><path d="M1 6h10M2 3.5h8M2 8.5h8" stroke="#1f4f8f" stroke-width="0.8"/></svg>
      <span>www.<span class="web-domain">tallowmeadwealth</span>.com</span>
    </div>
  </div>
  <p class="disclosure">All securities offered through Harrowgate Capital, Inc. Oakhurst Lane, NJ. Member QOLTA/DWEM.<br>Advisory services provided through HC Advisory Services, Inc. an PBR Registered Investment Advisor.</p>
</section>

</body>
</html>
```